Promotion for Local Garage - Orvel Motorworks offering 10% off

We are after an A5 Colour Leaflet to promote our business Orvel Motorworks.

Orvel Motorworks is a local garage and we are about to launch a flyer campaign in the local area.

Services we provide:
Servicing, Repairs, Diagnostics, Clutches, Brakes, Exhaust for all makes and models of cars and vans.

10% discount for anyone who brings in this flyer with them.

Company contact details below:
Telephone 0151 3846172
Website www.orvelmotorworks-example.co.uk

Address
Unit 4 Hollin Workshops,
Brackwell Lane,
Fenwick Ind Estate,
Ellesmere Port,
CH64 9QP

Our Logo is attached

Target Market(s)

Local Residents and businesses

Industry/Entity Type

Auto Repair

Requirements
Must have
• Services we provide:
• Servicing, Repairs, Diagnostics, Clutches, Brakes, Exhaust for all makes and models of cars and vans.
• 10% discount for anyone who brings in this flyer with them.
• Company contact details below:
• Telephone 0151 3846172
• Website www.orvelmotorworks-example.co.uk
• Address
• Unit 4 Hollin Workshops,
• Brackwell Lane,
• Fenwick Ind Estate,
• Ellesmere Port,
• CH64 9QP

```html
<!DOCTYPE html>
<html lang="en">
<head>
<meta charset="utf-8">
<title>Orvel Motorworks – A5 Leaflet</title>
<link rel="stylesheet" href="https://fonts.googleapis.com/css2?family=Oswald:wght@300;400;500;600;700&family=Open+Sans:wght@400;700&family=Roboto+Condensed:wght@400;700&display=swap">
<style>
  :root {
    --red: #e31b23;
    --deep-red: #b3171d;
    --grey: #555557;
    --dark-grey: #4a4a4c;
    --text-grey: #4d4d4f;
    --white: #ffffff;
    --page-bg: #eeeeee;
  }
  * { margin: 0; padding: 0; box-sizing: border-box; }
  html, body { width: 1200px; height: 1200px; overflow: hidden; background: var(--page-bg); }
  .canvas { position: relative; width: 1200px; height: 1200px; }
  .leaflet {
    position: absolute; left: 204px; top: 40px;
    width: 819px; height: 1160px;
    transform: scale(0.9655); transform-origin: top left;
    background: var(--white); overflow: hidden;
    box-shadow: 0 6px 24px rgba(0,0,0,.18);
  }
  .shapes { position: absolute; inset: 0; }
  .abs { position: absolute; white-space: nowrap; }

  .brand-name {
    right: 108px; top: 104px;
    font-family: "Oswald", sans-serif; font-weight: 500; font-size: 34px;
    color: var(--text-grey); letter-spacing: 1px; line-height: 1.2;
  }

  .car-photo {
    left: 300px; top: 170px; width: 440px; height: 240px;
    border-radius: 60px 90px 30px 40px;
    background: radial-gradient(ellipse at 55% 45%, #ee2a2f, #c3141c 60%, #7a0c12);
  }

  .badge-text { left: 36px; width: 280px; text-align: center; color: var(--white); font-family: "Oswald", sans-serif; }
  .badge-pct { top: 140px; font-size: 72px; font-weight: 700; line-height: 1; }
  .badge-small { font-size: 19px; font-weight: 500; line-height: 1; }
  .badge-discount { top: 213px; left: 110px; width: 180px; text-align: right; }
  .badge-anyone { top: 234px; font-size: 32px; font-weight: 600; line-height: 1; }
  .badge-brings { top: 277px; font-size: 16px; }
  .badge-them { top: 300px; font-size: 29px; font-weight: 600; line-height: 1; }

  .services-title {
    left: 56px; top: 462px;
    font-family: "Oswald", sans-serif; font-weight: 700; font-size: 38px;
    color: var(--white); letter-spacing: -0.5px; line-height: 1;
  }
  .service-list { list-style: none; }
  .service-item {
    position: absolute;
    font-family: "Oswald", sans-serif; font-weight: 600; font-size: 18px;
    color: var(--white); line-height: 1; padding-left: 24px;
  }
  .service-item::before {
    content: ""; position: absolute; left: 0; top: 7px;
    width: 6px; height: 6px; border-radius: 50%; background: var(--red);
  }
  .exhaust-note {
    left: 57px; top: 638px;
    font-family: "Open Sans", sans-serif; font-size: 17px; line-height: 24px;
    color: var(--white);
  }
  .call-label {
    left: 55px; top: 702px;
    font-family: "Open Sans", sans-serif; font-size: 34px; color: var(--white); line-height: 1;
  }
  .call-number {
    left: 52px; top: 752px;
    font-family: "Oswald", sans-serif; font-weight: 700; font-size: 38px; color: var(--white); line-height: 1;
  }

  .headline { right: 57px; text-align: right; color: var(--white); line-height: 1; }
  .headline-name { top: 484px; font-family: "Oswald", sans-serif; font-weight: 700; font-size: 54px; letter-spacing: 4px; }
  .headline-sub { top: 555px; font-family: "Open Sans", sans-serif; font-weight: 700; font-size: 31px; }
  .headline-local { top: 606px; font-family: "Oswald", sans-serif; font-weight: 700; font-size: 74px; letter-spacing: -1px; }
  .headline-garage { top: 692px; font-family: "Oswald", sans-serif; font-weight: 700; font-size: 104px; letter-spacing: -2px; }

  .work-photo {
    position: absolute; top: 832px; width: 196px; height: 144px;
    border: 6px solid var(--white);
    box-shadow: 0 10px 14px rgba(0,0,0,.18);
  }
  .work-photo--under { left: 363px; background: linear-gradient(135deg, #2b2d33, #4b5566 55%, #1f4aa0); }
  .work-photo--grinding { left: 588px; background: linear-gradient(135deg, #3a3c40, #5a4a3e 55%, #d8822a); }

  .address-title {
    left: 61px; top: 946px;
    font-family: "Roboto Condensed", sans-serif; font-weight: 700; font-size: 21px; color: #222;
  }
  .address-lines {
    left: 59px; top: 976px; font-style: normal;
    font-family: "Roboto Condensed", sans-serif; font-weight: 700; font-size: 20px;
    line-height: 28px; color: #5a5a5a;
  }
  .website {
    right: 66px; top: 1087px;
    font-family: "Oswald", sans-serif; font-weight: 500; font-size: 20px; color: var(--red);
  }
</style>
</head>
<body>
<div class="canvas">
  <article class="leaflet">
    <svg class="shapes" width="819" height="1160" viewBox="0 0 819 1160" aria-hidden="true">
      <defs>
        <linearGradient id="ringGrad" x1="0" y1="0" x2="1" y2="1">
          <stop offset="0" stop-color="#d9d9d9"/>
          <stop offset="0.5" stop-color="#8e8e8e"/>
          <stop offset="1" stop-color="#e6e6e6"/>
        </linearGradient>
        <radialGradient id="shadowGrad" cx="0.5" cy="0.5" r="0.5">
          <stop offset="0" stop-color="#000" stop-opacity=".28"/>
          <stop offset="1" stop-color="#000" stop-opacity="0"/>
        </radialGradient>
      </defs>
      <ellipse cx="500" cy="405" rx="300" ry="24" fill="url(#shadowGrad)"/>
      <polygon points="0,422 563,422 266,850 0,850" fill="var(--grey)"/>
      <polygon points="616,422 819,422 819,850 306,850" fill="var(--red)"/>
      <polygon points="0,858 270,858 282,875 0,875" fill="var(--red)"/>
      <rect x="306" y="860" width="513" height="18" fill="var(--dark-grey)"/>
      <rect x="0" y="1138" width="819" height="22" fill="var(--red)"/>
    </svg>

    <div class="abs brand-name">Orvel Motorworks</div>

    <div class="abs car-photo" role="img" aria-label="Photo of a red sports coupe"></div>

    <svg class="shapes" width="819" height="1160" viewBox="0 0 819 1160" aria-hidden="true">
      <circle cx="176" cy="235" r="140" fill="url(#ringGrad)"/>
      <circle cx="176" cy="235" r="126" fill="var(--deep-red)"/>
    </svg>

    <div class="abs badge-text badge-pct">10%</div>
    <div class="abs badge-text badge-small badge-discount">discount</div>
    <div class="abs badge-text badge-anyone">FOR ANYONE</div>
    <div class="abs badge-text badge-small badge-brings">who brings in this flyer</div>
    <div class="abs badge-text badge-them">WITH THEM</div>

    <h2 class="abs services-title">SERVICES WE PROVIDE:</h2>
    <ul class="service-list">
      <li class="service-item" style="left:58px;top:525px;">SERVICING</li>
      <li class="service-item" style="left:245px;top:525px;">BRAKES</li>
      <li class="service-item" style="left:57px;top:562px;">DIAGNOSTICS</li>
      <li class="service-item" style="left:245px;top:562px;">REPAIRS</li>
      <li class="service-item" style="left:59px;top:598px;">CLUTCHES</li>
    </ul>
    <p class="abs exhaust-note">EXHAUST FOR ALL MAKES AND<br>MODELS OF CARS AND VANS.</p>
    <div class="abs call-label">CALL US</div>
    <div class="abs call-number">0151 3846172</div>

    <div class="abs headline headline-name">ORVEL</div>
    <div class="abs headline headline-sub">MOTORWORKS</div>
    <div class="abs headline headline-local">IS LOCAL</div>
    <div class="abs headline headline-garage">GARAGE</div>

    <div class="work-photo work-photo--under" role="img" aria-label="Photo of a mechanic working underneath a raised car"></div>
    <div class="work-photo work-photo--grinding" role="img" aria-label="Photo of a mechanic grinding a car panel with sparks"></div>

    <div class="abs address-title">ADDRESS</div>
    <address class="abs address-lines">
      Unit 4 Hollin Workshops,<br>
      Brackwell Lane,<br>
      Fenwick Ind Estate,<br>
      Ellesmere Port,<br>
      CH64 9QP
    </address>
    <div class="abs website">www.orvelmotorworks-example.co.uk</div>
  </article>
</div>
</body>
</html>
```